2 menu designs: Tarn Hospitality

I have 2 restaurants that are going though large menu changes. I wanted them to have a style change as well!
-one is a steakhouse menu: must fit in two portrait legal pages. there is a picture of the menu book attached. The emphasis of the menu should be on the "steaks" and "prime rib". attached are menu items that need to be included
-the other is a burger restaurant: must fit on one legal landscape page. The focus of this menu should go to the middle of the page and emphasis "burgers" and "fries". attached is the general layout I'm interested in and the menu items that need to be included. Logo for restaurant is also included. picture of restaurant included

Both must be able to be edited often but the number of items and general placement of these items will not change

Industry/Entity Type

Hospitality

```html
<!DOCTYPE html>
<html lang="en">
<head>
<meta charset="utf-8">
<title>Tarn Hospitality Steakhouse Menu</title>
<link rel="stylesheet" href="https://fonts.googleapis.com/css2?family=Tinos:wght@400;700&family=Michroma&family=Questrial&display=swap">
<style>
  :root{
    --rust:#c4762f;
    --rust-deep:#a95e22;
    --band:#e9a93c;
    --cream:#fdf3d6;
    --cream-light:#fffaea;
    --gold:#f2b838;
    --card:#f8c76a;
    --red:#d22a2a;
    --ink:#111111;
  }
  *{margin:0;padding:0;box-sizing:border-box;}
  html,body{width:729px;height:1200px;overflow:hidden;background:var(--rust);}
  .menu{position:relative;width:729px;height:1200px;background:var(--rust);font-family:"Tinos",serif;color:var(--ink);}
  .frame{position:absolute;left:12px;top:10px;width:705px;height:1180px;border:6px solid var(--band);border-radius:6px;}
  .page{position:absolute;left:26px;top:24px;width:677px;height:1149px;
    background:radial-gradient(ellipse at 50% 45%,var(--cream-light) 0%,var(--cream) 70%);}
  .abs{position:absolute;}
  .center{left:0;width:729px;text-align:center;}

  .prime-card{background:var(--card);border-radius:14px;width:254px;height:193px;top:125px;text-align:center;}
  .prime-card .cut{font-weight:700;font-size:23px;margin-top:58px;letter-spacing:.3px;}
  .prime-card .cut small{font-size:19px;}
  .prime-card .price{font-weight:700;font-size:31px;margin-top:12px;}
  .prime-head{left:188px;top:86px;width:363px;height:62px;background:var(--gold);text-align:center;}
  .prime-head h1{color:var(--red);font-size:26px;font-weight:700;margin-top:7px;letter-spacing:.5px;}
  .prime-head p{color:var(--red);font-size:9.5px;font-weight:700;margin-top:2px;font-family:"Questrial",sans-serif;}

  .section-title{color:var(--red);font-size:21px;font-weight:700;}
  .intro{font-size:10.5px;font-weight:700;line-height:15px;}
  .intro .hl{color:var(--red);}

  .option-box{border:2px solid var(--red);width:166px;height:120px;text-align:center;font-weight:700;font-size:13px;line-height:26px;padding-top:10px;}
  .option-box .label{text-decoration:underline;}

  .steak{font-weight:700;font-size:11px;left:239px;}
  .steak .size{font-weight:400;}
  .note{color:var(--red);font-size:12.5px;}

  .sides-title{font-family:"Michroma",sans-serif;font-size:16px;letter-spacing:.5px;}
  .item{width:250px;}
  .item h3{font-size:10.5px;font-weight:700;line-height:13px;}
  .item p{font-size:10.5px;line-height:13px;}

  .entrees-box{left:98px;top:875px;width:533px;height:210px;border:1.5px solid var(--ink);}
  .entrees-label{left:263px;top:858px;width:210px;height:35px;background:var(--gold);text-align:center;
    font-family:"Questrial",sans-serif;color:var(--red);font-size:27px;letter-spacing:1px;line-height:35px;}
  .entree{width:225px;}
  .entree h3{font-size:10.5px;font-weight:700;line-height:13px;}
  .entree h3 span{font-weight:400;}
  .entree p{font-size:10.5px;line-height:13px;}
</style>
</head>
<body>
<div class="menu">
  <div class="frame"></div>
  <div class="page"></div>

  <div class="abs prime-card" style="left:106px;">
    <div class="cut">QUEEN CUT 14<small>oz</small></div>
    <div class="price">$28.95</div>
  </div>
  <div class="abs prime-card" style="left:369px;">
    <div class="cut">PRINCESS CUT 9<small>oz</small></div>
    <div class="price">$22.95</div>
  </div>
  <div class="abs prime-head">
    <h1>PRIME RIB</h1>
    <p>Featuring Heritage Select Beef ®</p>
  </div>

  <h2 class="abs center section-title" style="top:362px;">FROM THE BROILER</h2>
  <p class="abs center intro" style="top:404px;">OUR ANGUS STEAKS ARE SERVED A LA CARTE<br>WITH &nbsp;OUR <span class="hl">SEA SALT &amp; CRUSHED PEPPERCORN RUB</span>,</p>

  <div class="abs option-box" style="left:50px;top:448px;">
    <div class="label">RUBS &amp; SAUCES</div><div>PEPPERCORN</div><div>RED WINE</div><div>SIGNATURE</div>
  </div>
  <div class="abs option-box" style="left:509px;top:450px;">
    <div class="label">ADD ONS</div><div>LOBSTER</div><div>SHRIMP</div>
  </div>

  <div class="abs steak" style="top:467px;">STEAK FRITES AU POIVRE <span class="size">&nbsp;6oz</span> &nbsp;$19.95</div>
  <div class="abs steak" style="top:496px;">NY STRIP <span class="size">&nbsp;16oz</span> &nbsp;$38.95</div>
  <div class="abs steak" style="top:525px;">CENTER CUT FILET <span class="size">8oz</span> &nbsp;$30.95 | <span class="size">12oz</span> &nbsp;$34.95</div>
  <div class="abs steak" style="top:554px;">RIB EYE <span class="size">&nbsp;16oz</span> &nbsp;$33.95</div>

  <p class="abs center note" style="top:582px;">HSB® = Featuring Heritage Select Beef ®</p>

  <h2 class="abs center sides-title" style="top:616px;">SEASONAL SIDES</h2>

  <div class="abs item" style="left:104px;top:663px;"><h3>CREAMED SPINACH $6</h3><p>Bacon Shallot Crumble</p></div>
  <div class="abs item" style="left:104px;top:701px;"><h3>BLACK TRUFFLE MAC &amp; CHEESE $8</h3><p>Micro Broccoli</p></div>
  <div class="abs item" style="left:104px;top:745px;"><h3>STEAMED ASPARAGUS $7</h3><p>Garlic Streusel, Lemon Vinaigrette</p></div>
  <div class="abs item" style="left:104px;top:784px;"><h3>ROASTED MUSHROOMS $6</h3><p>Onion Thyme Jus</p></div>

  <div class="abs item" style="left:391px;top:657px;"><h3>HORSERADDISH OR CLASSIC WHIPPED<br>POTATOES $6</h3><p>Creamery Butter</p></div>
  <div class="abs item" style="left:391px;top:713px;"><h3>SALT BAKED POTATO $6</h3><p>White Cheddar Fondue, Scallions, Smoked Bacon</p></div>
  <div class="abs item" style="left:391px;top:751px;"><h3>DUCK FAT FRIES $6</h3><p>Sea Salt, Cracked Pepper</p></div>
  <div class="abs item" style="left:391px;top:789px;"><h3>MARKET BEST $6</h3><p>Farm To Table, Changes Daily</p></div>

  <div class="abs entrees-box"></div>
  <div class="abs entrees-label">ENTREES</div>

  <div class="abs entree" style="left:120px;top:929px;"><h3>SEARED PACIFIC SALMON <span>&nbsp;$24</span></h3><p>Grain Mustard Bearnaise, Seasonal Succotash</p></div>
  <div class="abs entree" style="left:120px;top:968px;"><h3>VEGETABLE MIXED GRILL $15</h3><p>Basil Balsamic, Herbed Goat Cheese Crepe</p></div>
  <div class="abs entree" style="left:120px;top:1008px;"><h3>PETALUMA BRICK CHICKEN $19</h3><p>Baby Carrot And Pea Tendril Salad, Roast Chicken Jus</p></div>

  <div class="abs entree" style="left:364px;top:923px;"><h3>TARNSIDE FRISCO MELT</h3><p>Hand Pressed Patty, Grilled Sourdough, White Cheddar, Caramelized Onion, Not So Secret Sauce,</p></div>
  <div class="abs entree" style="left:364px;top:975px;"><h3>STEAKHOUSE BURGER</h3><p>Hand Pressed Patty, Brioche Bun, Lettuce, Tomato, Onion</p></div>
  <div class="abs entree" style="left:364px;top:1032px;"><h3>DOUBLE CUT PORK CHOP <span>&nbsp;$21</span></h3><p>Creamed Cipolini, Pork Jus</p></div>
</div>
</body>
</html>
```